Minimalist, Flat(Matte) design for a Beef Jerky packaging company. No bullshit company looking for a

Need a packaging design for a new Beef Jerky product(in English). The name of the company is 'Vellorn' and thus the packaging should reflect the bullish, tough, and simple nature of the beef jerky product. The finished product should communicate simplicity, minimalism, yet toughness and strength.

The logo should be simple, with a minimal number of colors , and should be either all white/cream, or have some red as well. Main colors should be white, cream, tinted red, and matte black. I think 4 colors max would be best. The closest example to an existing package style would be Kessip Noir clove cigarettes( image attached).

It will be on a matte black standing pouch package. See image for package type. Package dimensions:

Dimension: Width x Gusset x Height
INCH : 5.125" (W) x 3.125" (G) x 8.125" (H)
MILLIMETER : 130mm (W) x 80mm (G) x 205mm (H)

I don't have anything totally specific so artistic liberty is encouraged, provided the colors are kept to a minimum and looks consistent with the simple nature of the brand and the matte black packaging.

Also attached an existing beef jerky package with a similar style to what we're looking for.

Industry/Entity Type

It Company

Colors
f59195
ffffff

Requirements
Must have
• Low contrast, flat and minimalist design.
Should not have
• A complicated design with many colors. Gawdy/flashy design. Bright colors. High contrast.

```html
<!DOCTYPE html>
<html lang="en">
<head>
<meta charset="utf-8">
<title>Vellorn Beef Jerky Pouch</title>
<link rel="stylesheet" href="https://fonts.googleapis.com/css2?family=Archivo:wght@400;700;900&family=Pinyon+Script&display=swap">
<style>
  :root {
    --backdrop: #ececec;
    --matte-black: #1e1e20;
    --zip-black: #2a2a2c;
    --seam: #111113;
    --blush: #f59195;
    --blush-deep: #ee6f78;
    --silver-light: #d9d9d9;
    --silver-dark: #6f6f72;
    --soft-white: #e8e8e8;
    --muted-grey: #8a8a8d;
  }
  * { margin: 0; padding: 0; box-sizing: border-box; }
  html, body {
    width: 1200px;
    height: 1200px;
    overflow: hidden;
    background: var(--backdrop);
  }
  .canvas {
    position: relative;
    width: 1200px;
    height: 1200px;
    background: var(--backdrop);
    font-family: "Archivo", Arial, sans-serif;
  }
  .pouch {
    position: absolute;
    left: 282px;
    top: 84px;
    width: 636px;
    height: 1032px;
    background: var(--matte-black);
    overflow: hidden;
  }
  .zip-strip {
    position: absolute;
    left: 0; top: 0;
    width: 100%;
    height: 44px;
    background: var(--zip-black);
  }
  .zip-seam {
    position: absolute;
    left: 0;
    width: 100%;
    height: 2px;
    background: var(--seam);
  }
  .zip-seam.upper { top: 80px; }
  .zip-seam.lower { top: 104px; }

  .origin-badge {
    position: absolute;
    left: 66px;
    top: 190px;
    width: 88px;
    height: 58px;
    border: 2px solid var(--muted-grey);
    border-radius: 4px;
  }
  .origin-note {
    position: absolute;
    left: 66px;
    top: 258px;
    font-size: 9px;
    letter-spacing: 0.5px;
    color: var(--muted-grey);
    white-space: nowrap;
  }

  .brand {
    position: absolute;
    left: 0;
    top: 196px;
    width: 100%;
    display: flex;
    flex-direction: column;
    align-items: center;
    gap: 22px;
  }
  .brand-square {
    width: 44px;
    height: 44px;
    background: var(--soft-white);
  }
  .brand-name {
    font-weight: 700;
    font-size: 26px;
    letter-spacing: 1px;
    color: var(--soft-white);
  }

  .product-tag {
    position: absolute;
    left: 0;
    top: 395px;
    width: 100%;
    display: flex;
    justify-content: center;
    align-items: center;
    gap: 18px;
    font-size: 27px;
    font-weight: 400;
    color: var(--soft-white);
    letter-spacing: 0.5px;
  }
  .dot-rule {
    width: 84px;
    height: 4px;
    background: radial-gradient(circle, var(--blush) 1.6px, transparent 2px) 0 0 / 10px 4px repeat-x;
  }

  .product-title {
    position: absolute;
    left: 0;
    top: 430px;
    width: 100%;
    text-align: center;
    font-weight: 900;
    font-size: 142px;
    line-height: 124px;
    letter-spacing: -2px;
    background: linear-gradient(135deg, var(--silver-light) 0%, var(--silver-dark) 45%, var(--silver-light) 70%, var(--silver-dark) 100%);
    -webkit-background-clip: text;
    background-clip: text;
    color: transparent;
  }

  .flavour {
    position: absolute;
    left: 0;
    top: 670px;
    width: 100%;
    text-align: center;
    font-family: "Pinyon Script", cursive;
    font-size: 112px;
    line-height: 130px;
    color: var(--blush);
    transform: rotate(-6deg);
  }

  .net-weight {
    position: absolute;
    left: 0;
    top: 808px;
    width: 100%;
    text-align: center;
    font-size: 15px;
    font-weight: 700;
    letter-spacing: 1px;
    color: #ffffff;
  }

  .accent-band {
    position: absolute;
    left: 0;
    top: 846px;
    width: 100%;
    height: 78px;
    background: linear-gradient(90deg, var(--blush-deep) 0%, var(--blush) 35%, #f7b1b5 50%, var(--blush) 65%, var(--blush-deep) 100%);
  }
</style>
</head>
<body>
  <main class="canvas">
    <section class="pouch">
      <div class="zip-strip"></div>
      <div class="zip-seam upper"></div>
      <div class="zip-seam lower"></div>

      <div class="origin-badge"></div>
      <p class="origin-note">NO NITRATES • NO MSG</p>

      <div class="brand">
        <span class="brand-square"></span>
        <span class="brand-name">VELLORN</span>
      </div>

      <div class="product-tag">
        <span class="dot-rule"></span>
        <span>HAND-CRAFTED</span>
        <span class="dot-rule"></span>
      </div>

      <h1 class="product-title">BEEF<br>JERKY</h1>

      <p class="flavour">Original</p>

      <p class="net-weight">NET WT. 3 OZ (85G)</p>

      <div class="accent-band"></div>
    </section>
  </main>
</body>
</html>
```